Standing Poster outside K Hotel

Hi, I have attached the picture of the existing poster which is self explanatory. The size of the poster is also attached in the instruction.

As usual, The design has to be catchy for guest from the K Hotel to be diverted to our restaurant along the same stretch. I have attached pictures of;

a. Asian food
b. Happy Family pic
c. Chef Artistic Pic
d. Pizzas pic
e. Pasta Artistic pic
f. Lorvo restaurant logo
g. Resto pic (requires cropping)
h.View pic
i. Poster sizing instructions
j. Sample poster
k. Seafood pic

Hope you can help us do a good one....

```html
<!DOCTYPE html>
<html lang="en">
<head>
<meta charset="utf-8">
<title>Lorvo Cafe – Chef's Recommendations Poster</title>
<link href="https://fonts.googleapis.com/css2?family=Dancing+Script:wght@600&family=Tinos:wght@400;700&display=swap" rel="stylesheet">
<style>
  :root {
    --page-bg: #f2f2f2;
    --peach: #f6dbc0;
    --peach-light: #fbeee1;
    --slate: #4b5059;
    --tan: #c89f82;
    --ink: #3a3a3a;
    --white: #ffffff;
  }
  * { margin: 0; padding: 0; box-sizing: border-box; }
  html, body {
    width: 1200px; height: 854px; overflow: hidden;
    background: var(--page-bg);
  }
  .poster {
    position: absolute; left: 262px; top: 22px;
    width: 676px; height: 810px; overflow: hidden;
    background:
      repeating-linear-gradient(90deg, rgba(255,255,255,0.22) 0 14px, rgba(255,255,255,0) 14px 30px),
      linear-gradient(180deg, var(--peach) 0%, var(--peach-light) 36%, var(--peach) 60%, var(--peach-light) 85%, var(--peach) 100%);
    box-shadow: 0 2px 6px rgba(0,0,0,0.12);
  }
  .frame { position: absolute; inset: 0; }
  .brand {
    position: absolute; left: 0; right: 0; top: 114px;
    text-align: center;
    font-family: "Tinos", serif; font-weight: 700;
    font-size: 34px; letter-spacing: 5px; color: var(--slate);
  }
  .headline {
    position: absolute; left: 0; right: 0; top: 244px;
    text-align: center;
    font-family: "Dancing Script", cursive; font-weight: 600;
    font-size: 38px; line-height: 50px; color: var(--slate);
  }
  .menu-strip {
    position: absolute; left: 0; top: 307px; width: 676px; height: 343px;
    display: flex; gap: 5px;
  }
  .menu-item { position: relative; flex: 1; height: 100%; }
  .menu-photo { position: absolute; inset: 0; }
  .menu-item--asian .menu-photo { background: linear-gradient(160deg, #6b4a35 0%, #c9a266 35%, #8a6a48 60%, #d9c47e 78%, #a8342a 100%); }
  .menu-item--pizza .menu-photo { background: linear-gradient(170deg, #3d3430 0%, #c4874f 30%, #d9a067 55%, #b36b3b 80%, #5a4a40 100%); }
  .menu-item--pasta .menu-photo { background: linear-gradient(165deg, #efe2b8 0%, #e3c86f 35%, #3f6b2e 60%, #b69a72 85%, #4b463e 100%); }
  .menu-item--seafood .menu-photo { background: linear-gradient(160deg, #3a6da0 0%, #d8532e 25%, #e8e3d6 50%, #4f7b2a 62%, #c2261c 85%, #9b1e17 100%); }
  .menu-label {
    position: absolute; left: 0; top: 14px;
    width: 86%; height: 28px; padding-left: 22px;
    background: var(--white);
    clip-path: polygon(0 0, 94% 0, 100% 100%, 0 100%);
    font-family: "Tinos", serif; font-size: 15px; letter-spacing: 0.5px;
    line-height: 28px; color: var(--tan);
  }
  .tagline {
    position: absolute; left: 104px; top: 630px; width: 480px; height: 48px;
  }
  .tagline-text {
    position: absolute; inset: 0;
    display: flex; align-items: center; justify-content: center;
    font-family: "Dancing Script", cursive; font-weight: 600;
    font-size: 22px; color: var(--white);
  }
  .contact {
    position: absolute; left: 0; right: 0; top: 700px;
    text-align: center; font-style: normal;
    font-family: "Tinos", serif; font-size: 16px; line-height: 25px;
    color: var(--ink);
  }
</style>
</head>
<body>
  <main class="poster">
    <svg class="frame" width="676" height="810" viewBox="0 0 676 810" aria-hidden="true">
      <path d="M48,12 H628 A30,30 0 0 0 658,42 V768 A30,30 0 0 0 628,798 H48 A30,30 0 0 0 18,768 V42 A30,30 0 0 0 48,12 Z"
            fill="none" stroke="#6b6260" stroke-width="1.3" stroke-dasharray="2 2"/>
    </svg>

    <div class="brand">LORVO CAFE</div>
    <h1 class="headline">Chef's Recommendations</h1>

    <section class="menu-strip">
      <div class="menu-item menu-item--asian">
        <div class="menu-photo" role="img" aria-label="Photo of Asian dishes: fried rice, seafood and crab"></div>
        <div class="menu-label">ASIAN FOOD</div>
      </div>
      <div class="menu-item menu-item--pizza">
        <div class="menu-photo" role="img" aria-label="Photo of several pizzas on a table"></div>
        <div class="menu-label">PIZZA</div>
      </div>
      <div class="menu-item menu-item--pasta">
        <div class="menu-photo" role="img" aria-label="Artistic photo of fresh pasta with vegetables and mushrooms"></div>
        <div class="menu-label">PASTA</div>
      </div>
      <div class="menu-item menu-item--seafood">
        <div class="menu-photo" role="img" aria-label="Photo of seafood platter with lobster, prawns and herb sauce"></div>
        <div class="menu-label">SEAFOOD</div>
      </div>
    </section>

    <div class="tagline">
      <svg width="480" height="48" viewBox="0 0 480 48" aria-hidden="true">
        <polygon points="4,6 476,0 468,22 478,44 2,48 10,28" fill="#4b5059"/>
        <polygon points="12,10 468,5 462,22 470,40 10,43 16,27" fill="none" stroke="#9aa0a8" stroke-width="1" stroke-dasharray="2 2"/>
        <circle cx="20" cy="26" r="2.5" fill="#ffffff"/>
        <circle cx="460" cy="22" r="2.5" fill="#ffffff"/>
      </svg>
      <div class="tagline-text">experience the spirit of the mediterranean</div>
    </div>

    <address class="contact">
      +65 61284470<br>
      18 Harbour Walk 02-14 Marina Quay Point<br>
      www.lorvocafe.com
    </address>
  </main>
</body>
</html>
```